Business Card Design

Copperfield Lantern Works, Inc. (CLW), located in Memphis, TN began operating on 2003. We are a certified
minority woman-owned business that genuinely takes a vested interest in our customers. We serve utilities,
government, contractors and end user markets in electrical, water, gas and industrial supplies. Our core
competency as a distributor of electrical materials has positioned us to serve business of all size. As your supply
chain partner, we arm you with the resources you need to make your supply chain more efficient. Our team
works with your team on a daily basis to help you solve problems and achieve goals. This team approach has
helped CLW customers to succeed and we can do the same for you.

NAICS Codes:
423610 Electrical Apparatus and Equipment, Wiring Supplies, and Related Equipment Merchant
Wholesalers
423510 Metal Service Centers and Other Metal Merchant Wholesalers
423720 Plumbing and Heating Equipment and Supplies (Hydronics) Merchant Wholesalers

Certifications
MBE (KRVPQAL, State of Tennessee Up-RFX and HJW), WBE (QOZRT),
WOSB, DOT (TDOT, MDOT, ALDOT, SCDOT, NCDOT, and VDOT), LOSB,
SBE, and LSB Certified
Some of Our Products Include:
. Boxes & Covers
. Conduit & Raceway
. Fittings
. Fuses
. Lamp & Ballasts
. Lighting Controls & Timers
. Lighting Fixtures
. Personal Safety
. Pipes
. Power Distribution
. Terminations Ground & Splices
. Tools & Testers
. Wire, Cords & Cable
. Wiring Devices
. Valves

Industry/Entity Type

Business

Contact Information for Business Card

Harriet M. Pendlow - President/CEO
4817 Galvin Ave., Memphis, TN 38127
901-482-6317 office, 901-482-6319 fax, 901-358-2074 cell
hmpendlow@clwgroupx.com - www.clwworksx.com

```html
<!DOCTYPE html>
<html lang="en">
<head>
<meta charset="utf-8">
<title>Copperfield Lantern Works — Business Card</title>
<link href="https://fonts.googleapis.com/css2?family=Source+Sans+3:wght@400;600&display=swap" rel="stylesheet">
<style>
  :root {
    --backdrop: #e8e5e0;
    --card-front: #ffffff;
    --card-back: #2b2b2b;
    --ink: #222222;
    --olive: #6e7a2c;
    --icon: #8a8460;
    --back-mark: #595959;
    --back-url: #7a7a7a;
  }
  * { margin: 0; padding: 0; box-sizing: border-box; }
  html, body { width: 1200px; height: 1000px; overflow: hidden; }
  body {
    background: var(--backdrop);
    font-family: "Source Sans 3", "Myriad Pro", Arial, sans-serif;
    color: var(--ink);
    position: relative;
  }
  .card {
    position: absolute;
    left: 265px;
    width: 666px;
    height: 397px;
  }
  .card-front { top: 73px; background: var(--card-front); }
  .card-back { top: 532px; background: var(--card-back); }

  .wordmark {
    position: absolute;
    display: flex;
    align-items: center;
    gap: 12px;
    text-transform: uppercase;
    font-weight: 400;
    line-height: 1.05;
  }
  .wordmark-dot { border-radius: 50%; flex: none; }
  .card-front .wordmark { left: 35px; top: 80px; font-size: 29px; color: var(--ink); }
  .card-front .wordmark-dot { width: 16px; height: 16px; background: var(--olive); }

  .address {
    position: absolute; left: 33px; top: 197px;
    font-size: 16px; line-height: 23px;
  }
  .contact-list {
    position: absolute; left: 33px; top: 256px;
    list-style: none; font-size: 16px;
  }
  .contact-list li {
    display: flex; align-items: center; gap: 9px; height: 23px;
  }
  .contact-list svg { width: 14px; height: 14px; fill: var(--icon); flex: none; }

  .person {
    position: absolute; right: 32px; top: 221px; text-align: right;
  }
  .person-name { font-size: 21px; font-weight: 600; color: var(--olive); line-height: 28px; }
  .person-title { font-size: 16px; line-height: 22px; }

  .card-back .wordmark {
    left: 0; right: 0; top: 170px; justify-content: center;
    font-size: 40px; color: var(--back-mark);
  }
  .card-back .wordmark-dot { width: 20px; height: 20px; background: var(--back-mark); }
  .back-url {
    position: absolute; left: 0; right: 0; top: 348px; text-align: center;
    font-size: 16px; letter-spacing: 2px; color: var(--back-url);
  }
</style>
</head>
<body>
  <section class="card card-front">
    <div class="wordmark">
      <span class="wordmark-dot"></span>
      <span class="wordmark-name">Copperfield Lantern<br>Works, Inc.</span>
    </div>

    <p class="address">4817 Galvin Ave., Memphis,<br>TN 38127</p>

    <ul class="contact-list">
      <li>
        <svg viewBox="0 0 14 14" aria-hidden="true"><rect x="4" y="0" width="6" height="14" rx="1"/><rect x="5" y="2" width="4" height="4" fill="#fff"/></svg>
        901-358-2074
      </li>
      <li>
        <svg viewBox="0 0 14 14" aria-hidden="true"><path d="M1 5c0-2 3-3 6-3s6 1 6 3v1H10V5H4v1H1z"/><rect x="2" y="7" width="10" height="6" rx="1"/></svg>
        901-482-6317
      </li>
      <li>
        <svg viewBox="0 0 14 14" aria-hidden="true"><rect x="3" y="1" width="8" height="4"/><rect x="1" y="5" width="12" height="6" rx="1"/><rect x="3" y="9" width="8" height="4" fill="#fff" stroke="#8a8460"/></svg>
        901-482-6319
      </li>
      <li>
        <svg viewBox="0 0 14 14" aria-hidden="true"><rect x="1" y="3" width="12" height="8"/><path d="M1 3l6 5 6-5" fill="none" stroke="#fff" stroke-width="1.2"/></svg>
        hmpendlow@clwgroupx.com
      </li>
      <li>
        <svg viewBox="0 0 14 14" aria-hidden="true"><circle cx="7" cy="7" r="6"/><path d="M1 7h12M7 1v12" stroke="#fff" stroke-width="1"/></svg>
        www.clwworksx.com
      </li>
    </ul>

    <div class="person">
      <p class="person-name">Harriet M. Pendlow</p>
      <p class="person-title">President / CEO</p>
    </div>
  </section>

  <section class="card card-back">
    <div class="wordmark">
      <span class="wordmark-dot"></span>
      <span class="wordmark-name">Copperfield Lantern<br>Works, Inc.</span>
    </div>
    <p class="back-url">www.clwworksx.com</p>
  </section>
</body>
</html>
```